Wine bottle label design for Coral Ridge Winery

We need a label design for our wine that is being sold in Sel Cay, Isle. We want it to be classic looking, a wine to be taken seriously. Not a whimsical Caribbean design with palm trees and beaches and waves... you get it. The story is about me, my dad and brother making wine for the past 12 years. We're of Italian heritage, so most of the grape varietals will reflect that (No, I don't want any images of Italy on the label :). The price point will be $22-25 retail, so the label should represent that. I have attached what I "threw together" for front/back. I like a simple clean look, black on white background, maybe with another rich accent color (I used hunter green). The back of the label will have a pic of me, my dad and brother. Aside from the "story" and the gov't warning, the design is open for interpretation.
Updates

Project Deadline Extended
Reason: Would like to see more designs different from the sample design I did and posted here.

Target Market(s)

Vistors and locals on the island of St. John who drink wine!

Font styles to use
Serif
Sans Serif

Requirements
Must have
• An upscale, but warm and inviting look and feel. Include logo in label design (Attached).
Nice to have
• It's okay if it's an all front label (See attached sample)
Should not have
• Palm trees, coconuts, waves, pictures grapes, vineyards, or leaves.

```html
<!DOCTYPE html>
<html lang="en">
<head>
<meta charset="utf-8">
<title>Coral Ridge Winery — Wine Label</title>
<link href="https://fonts.googleapis.com/css2?family=Playfair+Display:wght@700;900&family=Libre+Baskerville:wght@400;700&display=swap" rel="stylesheet">
<style>
  :root {
    --page: #ffffff;
    --label: #ffffff;
    --label-edge: #e4e4e4;
    --ink: #1c1c1c;
    --hunter: #2f6b34;
    --hunter-soft: #5f9a5e;
    --muted: #7a7a7a;
  }
  html, body {
    margin: 0;
    width: 813px;
    height: 1200px;
    overflow: hidden;
    background: var(--page);
  }
  .canvas {
    position: relative;
    width: 813px;
    height: 1200px;
  }
  .label {
    position: absolute;
    left: 66px;
    top: 130px;
    width: 680px;
    height: 900px;
    background: var(--label);
    border: 1px solid var(--label-edge);
    box-shadow: 0 2px 10px rgba(0,0,0,0.06);
  }
  .label__flourish {
    position: absolute;
    left: 70px;
    top: 150px;
    width: 120px;
    height: 330px;
    border-radius: 60px 60px 30px 30px;
    background: linear-gradient(170deg, var(--hunter-soft), var(--hunter));
  }
  .winery-name {
    position: absolute;
    left: 250px;
    top: 150px;
    font-family: "Libre Baskerville", serif;
    color: var(--ink);
  }
  .winery-name__main {
    display: block;
    font-size: 30px;
    letter-spacing: 1px;
  }
  .winery-name__sub {
    display: block;
    margin-top: 8px;
    font-size: 12px;
    letter-spacing: 6px;
    color: var(--muted);
    padding-left: 60px;
  }
  .region {
    position: absolute;
    left: 250px;
    top: 255px;
    margin: 0;
    font-family: "Playfair Display", serif;
    font-weight: 900;
    font-size: 84px;
    line-height: 0.98;
    color: var(--ink);
  }
  .vintage {
    position: absolute;
    left: 96px;
    top: 600px;
    font-family: "Libre Baskerville", serif;
    font-size: 26px;
    color: var(--hunter);
  }
  .varietals {
    position: absolute;
    left: 250px;
    top: 602px;
    font-family: "Libre Baskerville", serif;
    font-weight: 700;
    font-size: 22px;
    color: var(--hunter);
  }
  .side-note {
    position: absolute;
    top: 450px;
    font-family: "Libre Baskerville", serif;
    font-size: 11px;
    letter-spacing: 1px;
    color: var(--muted);
    white-space: nowrap;
  }
  .side-note--abv {
    left: 22px;
    transform: rotate(-90deg);
    transform-origin: left top;
  }
  .side-note--volume {
    right: 22px;
    transform: rotate(90deg);
    transform-origin: right top;
  }
</style>
</head>
<body>
<main class="canvas">
  <section class="label">
    <div class="label__flourish" role="img" aria-label="Green ornamental flourish"></div>

    <div class="winery-name">
      <span class="winery-name__main">CORAL RIDGE</span>
      <span class="winery-name__sub">WINERY</span>
    </div>

    <h1 class="region">SEL<br>CAY,<br>ISLE</h1>

    <div class="vintage">2014</div>
    <div class="varietals">Sangiovese · Cabernet</div>

    <span class="side-note side-note--abv">ALC. 13.5% VOL</span>
    <span class="side-note side-note--volume">750 ML</span>
  </section>
</main>
</body>
</html>
```